Bootstrap Website for Sports Technology Company

Create Bootstrap compatible, HTML and CSS stylesheet-based design templates for typography, forms, buttons, charts, navigation and other interface components for the www.quillmarsh-hub.example website. All designs should be Responsive CSS and Fluid.
We are transitioning www.quillmarsh-hub.example from Wordpress to Bootstrap and are looking for a fresh, clean landing page with navigation to other page styles. Official Colors and font are attached. Designer may recommend button styles, menu navigation, header, footer, etc. Please incorporate the graphic elements found on the quillmarsh-hub.example website.
Page Styles required:
- Landing Page
- Secondary Landing Page
- Five different Page Styles
- small, medium and large buttons
Designers are encouraged to submit the landing page with navigation. We will comment quickly to help with finalizing the design for final selection.

```html
<!DOCTYPE html>
<html lang="en">
<head>
<meta charset="utf-8">
<title>Quillmarsh – Landing Page</title>
<link href="https://fonts.googleapis.com/css2?family=Oswald:wght@300;400&display=swap" rel="stylesheet">
<style>
:root{
  --teal:#0ccbcc;
  --brand-blue:#3a63ad;
  --ink:#333333;
  --button-grey:#666666;
  --footer-grey:#6b6b6b;
  --footer-text:#f2f2f2;
  --white:#ffffff;
}
*{box-sizing:border-box;margin:0;padding:0}
html,body{width:1096px;height:1200px;overflow:hidden;background:var(--white)}
body{font-family:"Oswald",sans-serif;font-weight:300;color:var(--ink);position:relative}
a{color:inherit;text-decoration:none}

.site-header{position:absolute;left:0;top:0;width:1096px;height:124px}
.brand{position:absolute;left:181px;top:52px;display:flex;align-items:center;gap:8px;color:var(--brand-blue);font-size:28px;font-weight:400}
.brand-dot{width:22px;height:22px;border-radius:50%;background:#8a8a8a}
.main-nav{position:absolute;top:66px;right:140px;display:flex;align-items:center;font-size:15px;font-weight:300}
.main-nav a{display:block;height:27px;line-height:27px;padding:0 10px;color:#1d3340}
.main-nav a.is-active{background:var(--teal);color:var(--white)}
.main-nav .divider{padding:0 14px;color:#1d3340}

.hero{position:absolute;left:0;top:124px;width:1096px;height:496px;overflow:hidden}
.hero-photo{position:absolute;inset:0;background:linear-gradient(180deg,#c98a2a 0%,#e2a93a 18%,#6f5a2a 34%,#3f5a22 46%,#4d7a2c 65%,#3e6a26 100%)}
.hero-copy{position:absolute;left:181px;top:270px;width:560px;color:var(--white)}
.hero-title{font-size:34px;font-weight:300;line-height:44px;text-transform:uppercase;letter-spacing:-0.3px}
.hero-lead{font-size:19.5px;font-weight:300;line-height:31px;margin-top:4px}
.slider-nav{position:absolute;left:462px;top:446px;width:172px;height:24px;border-radius:12px;background:linear-gradient(#fafafa,#d8d8d8);box-shadow:0 1px 2px rgba(0,0,0,.35);display:flex;align-items:center;justify-content:space-between;padding:0 9px;font-size:10px;color:#888}
.slider-dots{display:flex;gap:6px}
.slider-dots span{width:6px;height:6px;border-radius:50%;background:#a9a9a9}
.slider-dots span.is-current{background:#0a8e8f}

.features{position:absolute;left:180px;top:662px;width:736px;height:270px}
.feature{position:absolute;top:0;width:235px}
.feature:nth-child(1){left:0}
.feature:nth-child(2){left:249px}
.feature:nth-child(3){left:501px}
.feature-tile{height:133px;background:var(--teal);display:flex;align-items:center;padding-left:30px;gap:22px;color:var(--white);font-size:29px;font-weight:300}
.feature-icon{width:60px;height:80px;background:rgba(255,255,255,.85);border-radius:4px;flex:none}
.feature-text{margin-top:18px;font-size:10.5px;line-height:18.7px;text-align:justify;letter-spacing:-0.1px}
.btn-more{position:absolute;top:236px;left:0;width:91px;height:30px;line-height:30px;text-align:center;background:var(--button-grey);color:var(--white);font-size:14px}

.site-footer{position:absolute;left:0;top:978px;width:1096px;height:222px;background:var(--footer-grey);color:var(--footer-text)}
.footer-col{position:absolute;top:36px}
.footer-col h3{font-size:15px;font-weight:400;margin-bottom:6px}
.footer-col li{list-style:none;font-size:11px;line-height:23.6px}
.col-portal{left:181px}
.col-who{left:350px}
.col-outreach{left:490px}
.col-info{left:741px}
.col-info li{line-height:18.7px}
.copyright{position:absolute;left:0;width:1096px;top:182px;text-align:center;font-size:11.5px}
.social{position:absolute;left:860px;top:175px;display:flex;gap:5px}
.social span{width:25px;height:25px;border-radius:50%;background:var(--white);display:flex;align-items:center;justify-content:center}
.page-code{position:absolute;left:1014px;top:182px;font-size:11.5px}
</style>
</head>
<body>
<header class="site-header">
  <a class="brand" href="#"><span class="brand-dot"></span>Quillmarsh</a>
  <nav class="main-nav">
    <a class="is-active" href="#">World</a><span class="divider">|</span>
    <a href="#">Golf</a><span class="divider">|</span>
    <a href="#">Club House</a>
  </nav>
</header>

<section class="hero">
  <div class="hero-photo" role="img" aria-label="Photo of a golf ball on a green fairway at sunset with trees behind"></div>
  <div class="hero-copy">
    <h1 class="hero-title">Sed ut perspiciatis unde omnis iste natus error sit voluptatem</h1>
    <p class="hero-lead">accusantium doloremque laudantium, totam rem aperiam, eaque ipsa quae ab illo inventore veritatis et quasi architecto beatae vitae dicta sunt explicabo.</p>
  </div>
  <div class="slider-nav">
    <span>&lsaquo;</span>
    <div class="slider-dots"><span></span><span class="is-current"></span><span></span><span></span><span></span></div>
    <span>&rsaquo;</span>
  </div>
</section>

<section class="features">
  <article class="feature">
    <div class="feature-tile"><div class="feature-icon" role="img" aria-label="Silhouette of a golfer putting"></div>Collect</div>
    <p class="feature-text">Lorem Ipsum is simply dummy text of the printing and typesetting industry. Lorem Ipsum has been the industry's standard dummy text ever since the 1500s, when an unknown printer took a galley</p>
    <a class="btn-more" href="#">Read More</a>
  </article>
  <article class="feature">
    <div class="feature-tile"><div class="feature-icon" role="img" aria-label="Circular arrows icon for analysis"></div>Analyze</div>
    <p class="feature-text">Lorem Ipsum is simply dummy text of the printing and typesetting industry. Lorem Ipsum has been the industry's standard dummy text ever since the 1500s, when an unknown printer took a galley</p>
    <a class="btn-more" href="#">Read More</a>
  </article>
  <article class="feature">
    <div class="feature-tile"><div class="feature-icon" role="img" aria-label="Device sending signal waves"></div>Instruct</div>
    <p class="feature-text">Lorem Ipsum is simply dummy text of the printing and typesetting industry. Lorem Ipsum has been the industry's standard dummy text ever since the 1500s, when an unknown printer took a galley</p>
    <a class="btn-more" href="#">Read More</a>
  </article>
</section>

<footer class="site-footer">
  <div class="footer-col col-portal"><h3>Quillmarsh Portal</h3><ul><li>Team Portal</li><li>Quillmarsh Exchange</li></ul></div>
  <div class="footer-col col-who"><h3>Who We Are</h3><ul><li>About us</li><li>Our Company</li><li>Product Development</li></ul></div>
  <div class="footer-col col-outreach"><h3>Outreach</h3><ul>
    <li>Quillmarsh Attends Hollowbrook Leadership Forum 2013</li>
    <li>Quillmarsh Attends Ridgeline Venture Summit 2013</li>
    <li>Ready to Tee Up First of Three Product Launches</li>
    <li>Quillmarsh Attends TechHum Spring 2013</li></ul></div>
  <div class="footer-col col-info"><h3>Other Information</h3><ul><li>Privacy Policy</li><li>Terms &amp; Conditions</li></ul></div>
  <p class="copyright">&copy; 2013 All Rights Reserved - Quillmarsh Enterprise, LLC</p>
  <div class="social">
    <span aria-label="Email"><svg width="14" height="10" viewBox="0 0 14 10"><rect x="0.5" y="0.5" width="13" height="9" fill="none" stroke="#6b6b6b"/><path d="M0.5 0.5 L7 5.5 L13.5 0.5" fill="none" stroke="#6b6b6b"/></svg></span>
    <span aria-label="Social link"></span>
    <span aria-label="Social link"></span>
    <span aria-label="Social link"></span>
  </div>
  <span class="page-code">C5</span>
</footer>
</body>
</html>
```